CORVID PRESS - Trade Show Flyer

Tri-fold brochure for trade show and follow-up mailings. Need design to mirror web-site look and feel. Use same color scheme of the blue and green. Please use a consistent font throughout. I like blocks of color or using the green/blue as border or trim.See the attachment for additional details, including specifications and content required.
Updates

Project Deadline Extended
Reason: Extended due to travel - company meetings

Target Market(s)

Business Professionals

Industry/Entity Type

Trade

Font styles to use
Serif
Sans Serif

Colors

Designer to choose colors to be used in the design.

Requirements
Must have
• A clean look and feel that matches our web-site
• Not too busy, white space is a plus
• Good use of color - blue and green (please match to web-site and attached logo colors)
Nice to have
• Icons or photos to break up the text
Should not have
• Should not be too busy or crowded. In the attached brief sheet, I included a section that can be removed if there is too much content.

```html
<!DOCTYPE html>
<html lang="en">
<head>
<meta charset="utf-8">
<title>Corvid Press – Trade Show Tri-fold</title>
<link href="https://fonts.googleapis.com/css2?family=Montserrat:ital,wght@0,400;0,500;0,600;0,700;1,400;1,500&display=swap" rel="stylesheet">
<style>
:root{
  --blue:#1f5a9e;
  --green:#1d9e55;
  --ink:#2b2b2b;
  --muted:#555;
  --paper:#ffffff;
  --bg:#e4e4e4;
  --photo-warm:linear-gradient(135deg,#6b4a36,#c79a7c 55%,#3a2a22);
  --photo-office:linear-gradient(135deg,#2c4f86,#8fa6c4 50%,#e6e1da);
  --photo-team:linear-gradient(135deg,#dfe3ea,#9aa8bc 50%,#3a4a63);
}
*{box-sizing:border-box;margin:0;padding:0}
html,body{width:1200px;height:1200px;overflow:hidden}
body{background:var(--bg);font-family:'Montserrat',sans-serif;color:var(--ink);position:relative}
.spread{position:absolute;left:60px;width:1080px;height:560px;background:var(--paper);display:flex;box-shadow:0 6px 18px rgba(0,0,0,.15)}
.spread--outside{top:30px}
.spread--inside{top:610px}
.panel{position:relative;width:360px;height:100%;overflow:hidden}
.panel+.panel{border-left:1px solid #eee}
.block{position:absolute;left:0;right:0}
.photo{position:absolute}
.green{background:var(--green);color:#fff}
.blue{background:var(--blue);color:#fff}
.quote-mark{font-size:54px;font-weight:700;line-height:1;height:36px;text-align:center;font-family:Georgia,serif}
.quote-text{font-size:10.5px;line-height:1.45;text-align:center}
.quote-by{font-size:10px;font-style:italic;text-align:right;margin-top:10px}
.brand{display:flex;align-items:center;justify-content:center;gap:10px;height:100%}
.brand__dot{width:14px;height:14px;border-radius:50%;background:var(--green)}
.brand__name{font-size:26px;font-weight:700;color:var(--blue);line-height:1.05;text-align:left}
.web{font-size:11px;text-align:center;line-height:60px;color:#fff}
.stuff{padding:22px 28px}
.stuff h3{font-size:12px;font-weight:700;letter-spacing:.04em;margin-bottom:8px}
.stuff ul{list-style:none;font-size:10.5px;line-height:1.6}
.stuff ul li::before{content:"• "}
.stuff em{display:block;font-size:10.5px;margin-top:8px;line-height:1.4}
.contact{padding:26px 34px;font-size:11px;line-height:1.45}
.contact h3{font-size:13px;font-weight:700;letter-spacing:.04em;margin-bottom:10px}
.contact .row{display:flex;gap:10px;align-items:flex-start;margin-bottom:6px}
.contact svg{flex:none;margin-top:2px}
.contact strong{font-weight:700}
.tagline-strip{position:absolute;left:0;top:0;width:92px;height:370px;background:var(--blue)}
.tagline-strip p{position:absolute;left:46px;top:185px;width:340px;transform:translate(-50%,-50%) rotate(-90deg);color:#fff;font-size:14px;font-weight:700;letter-spacing:.06em;line-height:1.3;text-align:center}
.section-title{font-size:12px;font-weight:700;letter-spacing:.05em;text-align:center;color:var(--ink)}
.dots{display:flex;justify-content:center;gap:3px;margin:6px 0 12px}
.dots i{width:6px;height:6px;border-radius:50%;background:var(--green)}
.intro{margin:0 24px;padding:16px 18px;font-size:10.5px;line-height:1.45}
.intro p+p{margin-top:10px}
.diff{margin:18px 24px 0}
.diff h4{font-size:12px;font-weight:700;line-height:1.3;margin-bottom:8px}
.feature{display:flex;align-items:center;gap:10px;font-size:10.5px;margin:5px 0 0 8px;line-height:1.3}
.feature svg{flex:none}
.call{margin:12px 24px 0;font-size:11px;font-style:italic;font-weight:500;text-align:center;line-height:1.35}
.mission-caption{position:absolute;left:0;right:0;top:196px;height:44px;background:var(--blue);color:#fff;font-size:12px;font-weight:600;padding:7px 24px;line-height:1.3}
.mission-list{position:absolute;top:256px;left:28px;right:26px;list-style:none;font-size:10.5px;line-height:1.4}
.mission-list li{margin-bottom:9px}
.mission-box{position:absolute;left:0;right:0;bottom:0;height:150px;padding:18px 26px;font-size:10.5px;line-height:1.4}
.mission-box p+p{margin-top:8px}
.services{padding:22px 24px}
.services .rule{height:1px;background:var(--blue);margin-top:10px}
.service{margin-top:12px}
.service__head{display:flex;align-items:center;justify-content:space-between}
.service__label{background:var(--green);color:#fff;font-size:11px;font-weight:700;padding:3px 10px;width:220px}
.service p{font-size:10px;line-height:1.4;margin-top:5px}
</style>
</head>
<body>

<!-- Outside spread -->
<section class="spread spread--outside" aria-label="Brochure outside">
  <div class="panel">
    <div class="block blue" style="top:0;height:170px;width:90px"></div>
    <div class="photo" role="img" aria-label="Smiling call center agent with a headset" style="left:60px;top:0;width:300px;height:170px;background:var(--photo-warm)"></div>
    <div class="block green" style="top:170px;height:235px;padding:18px 30px">
      <div class="quote-mark">“</div>
      <p class="quote-text">“Halden Group has used Corvid Press (HG) for twelve years for outbound appointment generation. Our company has grown multi-fold and we could not have done it without this fine organization. Jen and Tomas have catered to our every need and are extremely customer focused. You cannot hide results from appointment generated leads. They produce quality appointments for our company. We do not consider them our vendor, we view them as our best business partner.”</p>
      <p class="quote-by"><strong>Owen Hartley</strong>, Owner/Principal Halden Group</p>
    </div>
    <div class="block" style="top:405px;height:95px">
      <div class="brand"><span class="brand__dot"></span><span class="brand__name">Corvid<br>Press</span></div>
    </div>
    <div class="block blue web" style="top:500px;height:60px">www.corvidpress.com</div>
  </div>

  <div class="panel">
    <div class="block green stuff" style="top:0;height:170px">
      <h3>WE'VE GOT THE RIGHT STUFF</h3>
      <ul>
        <li>Focus on Service</li>
        <li>Quality Results</li>
        <li>Commitment to Fair Prices</li>
        <li>Proven track record</li>
        <li>Standards of excellence</li>
      </ul>
      <em>Once you experience our quality and service, you'll never settle for less.</em>
    </div>
    <div class="block" style="top:170px;height:220px;padding:16px 32px">
      <div class="quote-mark" style="color:var(--blue)">“</div>
      <p class="quote-text">“I love working with Mara Ellison at Corvid Press. She handles all of the details of my telemarketing project from scripts to approvals to reporting. We try many new lists and some are real lemons. Mara is great at analyzing what is good and bad about a campaign and coming up with inventive ways to make lemonade out of those lemons. I feel like she will always maximize whatever budget I have to spend on a campaign and does everything she can to help me reach my goals.”</p>
      <p class="quote-by" style="font-style:normal"><strong>Priya Lanford</strong>, Brookline Publishing</p>
    </div>
    <div class="block blue contact" style="top:390px;height:170px">
      <h3>CONTACT US</h3>
      <div class="row"><svg width="12" height="14" viewBox="0 0 12 14"><path d="M6 0a5 5 0 0 0-5 5c0 4 5 9 5 9s5-5 5-9a5 5 0 0 0-5-5z" fill="#fff"/><circle cx="6" cy="5" r="2" fill="var(--blue)"/></svg><span><strong>CORVID PRESS</strong><br>218 Alder Lane #4<br>Riverton, CO 80000</span></div>
      <div class="row"><svg width="12" height="12" viewBox="0 0 12 12"><circle cx="6" cy="6" r="5.3" fill="none" stroke="#fff" stroke-width="1.2"/><path d="M.7 6h10.6M6 .7c-3 3-3 7.6 0 10.6M6 .7c3 3 3 7.6 0 10.6" fill="none" stroke="#fff"/></svg><span>www.corvidpress.com</span></div>
      <div class="row"><svg width="12" height="12" viewBox="0 0 12 12"><rect x=".5" y="2" width="11" height="8" fill="#fff"/><path d="M.5 2l5.5 4.5L11.5 2" fill="none" stroke="var(--blue)"/></svg><span><strong>Mara Ellison,</strong> VP Business Development · mellison@corvidpress.com</span></div>
      <div class="row"><svg width="12" height="12" viewBox="0 0 12 12"><circle cx="6" cy="6" r="6" fill="#fff"/><path d="M3.5 3c.5 2.8 2.6 5 5.2 5.5l.6-1.3-1.5-.7-.6.6c-1-.4-1.8-1.2-2.2-2.2l.6-.6-.7-1.5z" fill="var(--blue)"/></svg><span>555-014-2290</span></div>
    </div>
  </div>

  <div class="panel">
    <div class="tagline-strip"><p>WORLD CLASS INNOVATION,<br>CLIENT CENTRIC SOLUTIONS &amp; SERVICES</p></div>
    <div class="photo" role="img" aria-label="Customer service agent with headset in a bright office" style="left:92px;top:0;width:268px;height:370px;background:var(--photo-office)"></div>
    <div class="block" style="top:370px;height:130px">
      <div class="brand"><span class="brand__dot"></span><span class="brand__name">Corvid<br>Press</span></div>
    </div>
    <div class="block green web" style="top:500px;height:60px">www.corvidpress.com</div>
  </div>
</section>

<!-- Inside spread -->
<section class="spread spread--inside" aria-label="Brochure inside">
  <div class="panel">
    <div style="padding-top:22px">
      <h2 class="section-title">GET THE COMPETITIVE ADVANTAGE</h2>
      <div class="dots"><i></i><i></i><i></i></div>
    </div>
    <div class="intro blue">
      <p>For the past 28 years Corvid Press has been helping clients meet their goals on time and within budget.</p>
      <p>With a changing marketplace, your telemarketing solutions have to be smarter, faster, better and more affordable. All without compromising quality.</p>
    </div>
    <div class="diff">
      <h4>Quality, service and innovation make the difference</h4>
      <div class="feature"><svg width="14" height="14" viewBox="0 0 14 14"><circle cx="7" cy="7" r="6" fill="none" stroke="var(--blue)" stroke-width="1.5"/><path d="M4 10l6-6" stroke="var(--blue)" stroke-width="1.5"/></svg>Greater Conversion Rates</div>
      <div class="feature"><svg width="14" height="14" viewBox="0 0 14 14"><rect x="3.5" y="1" width="7" height="12" rx="1" fill="none" stroke="var(--blue)" stroke-width="1.5"/></svg>Cell Phone Dialing</div>
      <div class="feature"><svg width="14" height="14" viewBox="0 0 14 14"><rect x="1" y="2" width="12" height="8" rx="1.5" fill="var(--blue)"/><path d="M3 10v3l3-3z" fill="var(--blue)"/><circle cx="4.5" cy="6" r="1" fill="#fff"/><circle cx="7" cy="6" r="1" fill="#fff"/><circle cx="9.5" cy="6" r="1" fill="#fff"/></svg>SMS Text Messaging</div>
      <div class="feature"><svg width="14" height="14" viewBox="0 0 14 14"><path d="M3 1h6l3 3v9H3z" fill="var(--blue)"/><path d="M5 6h5M5 8.5h5M5 11h5" stroke="#fff"/></svg>List Segmentation</div>
      <div class="feature"><svg width="14" height="14" viewBox="0 0 14 14"><path d="M1 3h3l6 8h3M1 11h3l6-8h3" fill="none" stroke="var(--blue)" stroke-width="1.5"/></svg>Cross Marketing</div>
      <div class="feature"><svg width="14" height="14" viewBox="0 0 14 14"><rect x="2" y="1" width="10" height="12" rx="1" fill="var(--blue)"/><path d="M5 4c.3 2.5 2 4.5 4.5 5l.5-1-1.2-.6-.5.5c-.8-.4-1.5-1-1.8-1.8l.5-.5L6.4 4z" fill="#fff"/></svg>Phone appends to bad &amp; disconnected numbers</div>
    </div>
    <p class="call">We're passionate about what we do – call us today to see how we can help you!</p>
    <div class="photo" role="img" aria-label="Three business colleagues reviewing a laptop together" style="left:0;right:0;bottom:0;height:128px;background:var(--photo-team)"></div>
  </div>

  <div class="panel">
    <div class="photo" role="img" aria-label="Two professionals working together at a desk" style="left:0;right:0;top:0;height:196px;background:var(--photo-office)"></div>
    <div class="mission-caption">At CORVID PRESS,<br>our mission and culture is clear:</div>
    <ul class="mission-list">
      <li>We use our experience to help you grow your business.</li>
      <li>We are client centric and results oriented.</li>
      <li>We consistently deliver a high quality product that is in compliance with industry standards.</li>
      <li>We strive to continuously serve your needs by providing innovative communication solutions to ensure you succeed.</li>
    </ul>
    <div class="mission-box green">
      <p>We use our pioneering spirit to professionally represent our clients, deliver valuable services and deliver an amazing client experience.</p>
      <p>We create value for our clients by exceeding their goals and expectations.</p>
      <p>From inbound to outbound, our agents aren't just trained to speak, we're trained to get the job done.</p>
    </div>
  </div>

  <div class="panel">
    <div class="services">
      <h2 class="section-title">SERVICES OFFERED</h2>
      <div class="dots" style="margin-bottom:0"><i></i><i></i><i></i></div>
      <div class="rule"></div>

      <div class="service">
        <div class="service__head"><span class="service__label">Circulation/Audience Development</span><svg width="22" height="20" viewBox="0 0 22 20"><path d="M2 2h18v12H9l-5 4v-4H2z" fill="none" stroke="var(--green)" stroke-width="1.5"/></svg></div>
        <p>We have earned our reputation as a high quality partner with a proven ability to increase conversion, reduce costs and meet goals and budgets.</p>
      </div>
      <div class="service">
        <div class="service__head"><span class="service__label">Event/Trade Show</span><svg width="22" height="20" viewBox="0 0 22 20"><rect x="2" y="3" width="18" height="15" fill="none" stroke="var(--green)" stroke-width="1.5"/><path d="M2 7h18M6 1v4M16 1v4M6 11h2M10 11h2M14 11h2M6 14h2M10 14h2" stroke="var(--green)" stroke-width="1.5"/></svg></div>
        <p>We understand how to make your next event, trade show, conference or seminar successful. Whether you need to cleanse data, increase attendance, market your venue, or conduct reminder calls or a post show survey – we can customize a solution that works.</p>
      </div>
      <div class="service">
        <div class="service__head"><span class="service__label">Lead Gen</span><svg width="22" height="20" viewBox="0 0 22 20"><path d="M4 18V9a7 7 0 0 1 14 0v9h-4V9a3 3 0 0 0-6 0v9z" fill="none" stroke="var(--green)" stroke-width="1.5"/></svg></div>
        <p>Penetrate your target accounts and engage with key decision makers. We maximize business sales leads and develop those not-ready-for engagement prospects into active sales prospects.</p>
      </div>
      <div class="service">
        <div class="service__head"><span class="service__label">Research</span><svg width="22" height="20" viewBox="0 0 22 20"><path d="M4 18l2-5L16 3l3 3L9 16z" fill="none" stroke="var(--green)" stroke-width="1.5"/></svg></div>
        <p>Our exceptional staff, training systems and marketing research expertise will provide you with a survey or polling package that is custom designed for your needs.</p>
      </div>
      <div class="service">
        <div class="service__head"><span class="service__label">BPO</span><svg width="22" height="20" viewBox="0 0 22 20"><path d="M2 18h18" stroke="var(--green)" stroke-width="1.5"/><rect x="4" y="11" width="3" height="7" fill="none" stroke="var(--green)"/><rect x="9" y="8" width="3" height="10" fill="none" stroke="var(--green)"/><rect x="14" y="5" width="3" height="13" fill="none" stroke="var(--green)"/><path d="M3 8l5-4 4 2 6-5" fill="none" stroke="var(--green)" stroke-width="1.2"/></svg></div>
        <p>Customized program to support your specific requirements. We provide a world class sales and marketing engine to drive your sales and decrease your costs. Results are measurable and reports provided to track progress.</p>
      </div>
    </div>
  </div>
</section>

</body>
</html>
```